Med Spa business card design with logo

Need a logo design and business card for our new company Verbena Aesthetics Med Spa. We are a medical office that deals with high end clients. We offer them skin care products which include DERMIQ, lip augmentation, and various laser for the skin. I king of like the logo attached, maybe something along those lines but also open to any logo concept.
Updates

Target Market(s)

Out target audience are male and females in the age range of 21-80 years of age

Industry/Entity Type

Medical

Contact Information for Business Card

woukd like front of card to have logo and business name VERBENA AESTHETICS MEDSPA. Back of card employee name and phone number along with instagram logo and user name

Font styles to use
Serif
Sans Serif

Requirements
Must have
• prefer monochromatic look white, black, gold
Should not have
• not too colorful

```html
<!DOCTYPE html>
<html lang="en">
<head>
<meta charset="utf-8">
<title>Verbena Aesthetics Med Spa – Business Card</title>
<link rel="stylesheet" href="https://fonts.googleapis.com/css2?family=Questrial&family=Lato:wght@400&display=swap">
<style>
  :root {
    --backdrop: #222222;
    --card-dark: #1f1e1f;
    --card-light: #ffffff;
    --ink: #1b1b1b;
    --white: #ffffff;
    --gold: #c8974a;
    --gold-light: #e9c46a;
    --gold-deep: #a8762e;
  }
  html, body {
    margin: 0;
    padding: 0;
    width: 1189px;
    height: 1200px;
    overflow: hidden;
    background: var(--backdrop);
  }
  .canvas {
    position: relative;
    width: 1189px;
    height: 1200px;
  }
  .card {
    position: absolute;
    left: 171px;
    width: 856px;
    height: 488px;
    border-radius: 24px;
    overflow: hidden;
  }
  .card--front { top: 67px; background: var(--card-dark); border: 1px solid #3a3a3a; box-sizing: border-box; }
  .card--back { top: 626px; background: var(--card-light); }
  .card svg { display: block; width: 856px; height: 488px; }
  .brand-name { font-family: "Questrial", sans-serif; }
  .body-text { font-family: "Lato", sans-serif; }
</style>
</head>
<body>
<div class="canvas">

  <section class="card card--front" aria-label="Card front">
    <svg viewBox="0 0 856 488" xmlns="http://www.w3.org/2000/svg">
      <circle class="brand-mark" cx="428" cy="153" r="73" fill="none" stroke="var(--gold)" stroke-width="2"/>
      <text class="brand-name" x="428" y="290" text-anchor="middle" font-size="55" fill="var(--white)">Verbena Aesthetics</text>
      <text class="brand-name" x="428" y="333" text-anchor="middle" font-size="41" fill="var(--white)">Med Spa</text>
      <text class="body-text" x="428" y="410" text-anchor="middle" font-size="21" fill="var(--white)">www.<tspan fill="var(--gold-light)">verbenamedspa</tspan>.com</text>
    </svg>
  </section>

  <section class="card card--back" aria-label="Card back">
    <svg viewBox="0 0 856 488" xmlns="http://www.w3.org/2000/svg">
      <circle class="accent-dot" cx="0" cy="81" r="30" fill="var(--gold)"/>

      <text class="body-text person-name" x="54" y="81" font-size="31" fill="var(--ink)">NORA WHITFIELD</text>
      <text class="body-text person-title" x="53" y="104" font-size="23" fill="var(--ink)">Director</text>

      <circle class="brand-mark" cx="632" cy="107" r="57" fill="none" stroke="var(--ink)" stroke-width="2"/>
      <text class="brand-name" x="633" y="216" text-anchor="middle" font-size="47" fill="var(--ink)">Verbena Aesthetics</text>
      <text class="brand-name" x="633" y="251" text-anchor="middle" font-size="34" fill="var(--ink)">Med Spa</text>

      <g class="contact-icons" fill="var(--gold)">
        <rect x="54" y="330" width="25" height="25" rx="4"/>
        <rect x="54" y="360" width="25" height="25" rx="4"/>
        <rect x="54" y="391" width="25" height="25" rx="4"/>
        <rect x="54" y="419" width="25" height="25" rx="4"/>
      </g>
      <g class="contact-glyphs" fill="none" stroke="var(--white)" stroke-width="1.6">
        <!-- phone -->
        <path d="M60 339 q6.5 -4 13 0 M61 341 h11 v7 h-11 z"/>
        <!-- fax -->
        <path d="M61 368 h11 v7 h-11 z M63 368 v-3 h7 v3 M63 375 v3 h7 v-3"/>
        <!-- envelope -->
        <path d="M59 397 h15 v12 h-15 z M59 397 l7.5 6 l7.5 -6"/>
        <!-- globe -->
        <circle cx="66.5" cy="431.5" r="7"/>
        <path d="M59.5 431.5 h14 M66.5 424.5 q-5 7 0 14 q5 -7 0 -14"/>
      </g>
      <g class="body-text contact-lines" font-size="24" fill="var(--ink)">
        <text x="85" y="349">(01) 5550 2840</text>
        <text x="85" y="379">(01) 5550 2840</text>
        <text x="85" y="410">hello@verbenamedspa.com</text>
        <text x="86" y="438">www.verbenamedspa.com</text>
      </g>

      <g class="body-text address" font-size="23" fill="var(--ink)" text-anchor="end">
        <text x="808" y="416">PO BOX 418 Linden Avenue</text>
        <text x="808" y="445">2nd street Hartford, USA</text>
      </g>
    </svg>
  </section>

</div>
</body>
</html>
```